Professional Home Buyer business card needed

I need a pretty straight forward business card designed. We help people that NEED to sell their homes solve problems. We perform all types of Real Estate transactions including flip, wholesale, investment, rental property and multi family. The card will mainly be used to give to prospective Sellers but will also be given to Real Estate Investors as well. It should professional and very easy to read, most clients are older people.

Target Market(s)

Distressed home sellers as well as Real Estate investors

Industry/Entity Type

Real Estate

Contact Information for Business Card

should be a professional layout

Colors
ec1f27
ffffff
000000

Requirements
Must have
• Large logo on back and smaller one on front. should utilize Red, white, and black.
• I am thinking of using a soft touch coating on the card so keep that in mind.
• Contact info should be very easy to read, think older clients.
Nice to have
• I would like to see a design with rounded corners on the card
Should not have
• pictures of homes or other home graphics.

```html
<!DOCTYPE html>
<html lang="en">
<head>
<meta charset="utf-8">
<title>Keystone Home Buyers – Business Card</title>
<link rel="stylesheet" href="https://fonts.googleapis.com/css2?family=Saira+Semi+Condensed:wght@400;600;800&display=swap">
<style>
  :root {
    --brand-red: #ec1f27;
    --brand-white: #ffffff;
    --brand-black: #000000;
    --card-black: #111111;
    --backdrop: #2b2d30;
    --type: "Saira Semi Condensed", sans-serif;
  }
  html, body {
    margin: 0;
    width: 1200px;
    height: 900px;
    overflow: hidden;
    background: var(--backdrop);
    font-family: var(--type);
  }
  .canvas {
    position: relative;
    width: 1200px;
    height: 900px;
  }
  .card {
    position: absolute;
    left: 250px;
    width: 700px;
    height: 400px;
    border-radius: 34px;
    overflow: hidden;
  }
  .card--front { top: 40px; background: var(--brand-white); }
  .card--back { top: 470px; background: var(--card-black); }

  .card__shapes { position: absolute; inset: 0; }

  .person {
    position: absolute;
    left: 44px;
    top: 34px;
    color: var(--brand-white);
  }
  .person__name {
    margin: 0;
    font-size: 40px;
    font-weight: 800;
    line-height: 1.05;
  }
  .person__title {
    margin: 2px 0 0;
    font-size: 26px;
    font-weight: 400;
  }

  .brand {
    position: absolute;
    text-align: center;
  }
  .brand__tagline {
    margin: 0;
    font-weight: 600;
    letter-spacing: 0.2em;
    text-transform: uppercase;
  }
  .brand__lockup {
    display: flex;
    align-items: center;
    justify-content: center;
  }
  .brand__name {
    margin: 0;
    font-weight: 800;
    text-transform: uppercase;
    line-height: 1.1;
    letter-spacing: 0.06em;
    text-align: left;
  }
  .brand__dot {
    display: inline-block;
    flex: none;
    background: var(--brand-red);
  }

  .card--front .brand {
    left: 390px;
    top: 44px;
    width: 300px;
  }
  .card--front .brand__tagline { font-size: 12px; color: var(--brand-black); margin-bottom: 12px; }
  .card--front .brand__lockup { gap: 12px; }
  .card--front .brand__name { font-size: 28px; color: var(--brand-black); }
  .card--front .brand__dot { width: 16px; height: 16px; }

  .contact {
    position: absolute;
    left: 44px;
    top: 214px;
    margin: 0;
    padding: 0;
    list-style: none;
    color: var(--brand-white);
    font-size: 22px;
  }
  .contact__item {
    display: flex;
    align-items: center;
    gap: 12px;
    margin-bottom: 10px;
  }
  .contact__icon { width: 20px; height: 20px; flex: none; }

  .address {
    position: absolute;
    right: 44px;
    bottom: 30px;
    margin: 0;
    text-align: right;
    color: var(--brand-white);
    font-style: normal;
    font-size: 24px;
    font-weight: 600;
    line-height: 1.25;
  }

  .card--back .brand {
    left: 0;
    right: 0;
    top: 112px;
  }
  .card--back .brand__tagline { font-size: 18px; color: var(--brand-white); margin-bottom: 22px; }
  .card--back .brand__lockup { gap: 22px; }
  .card--back .brand__name { font-size: 54px; color: var(--brand-white); }
  .card--back .brand__dot { width: 28px; height: 28px; }
</style>
</head>
<body>
<main class="canvas">

  <section class="card card--front" aria-label="Business card front">
    <svg class="card__shapes" viewBox="0 0 700 400" width="700" height="400" aria-hidden="true">
      <rect class="name-panel" x="0" y="0" width="380" height="200" fill="var(--brand-red)"/>
      <path class="accent-stripe-white" d="M0,108 Q380,128 700,278 L700,400 L0,400 Z" fill="var(--brand-white)"/>
      <path class="accent-stripe-red" d="M0,118 Q380,138 700,288 L700,400 L0,400 Z" fill="var(--brand-red)"/>
      <path class="contact-panel" d="M0,136 Q380,156 700,306 L700,400 L0,400 Z" fill="var(--card-black)"/>
    </svg>

    <div class="person">
      <h1 class="person__name">Daniel Hartley</h1>
      <p class="person__title">President</p>
    </div>

    <div class="brand">
      <p class="brand__tagline">Fair offers, fast closings</p>
      <div class="brand__lockup">
        <span class="brand__dot"></span>
        <p class="brand__name">Keystone<br>Home Buyers</p>
      </div>
    </div>

    <ul class="contact">
      <li class="contact__item">
        <svg class="contact__icon" viewBox="0 0 24 24" aria-hidden="true"><path d="M6.6 10.8a15 15 0 0 0 6.6 6.6l2.2-2.2a1 1 0 0 1 1-.25 11.4 11.4 0 0 0 3.6.57 1 1 0 0 1 1 1V20a1 1 0 0 1-1 1A17 17 0 0 1 3 4a1 1 0 0 1 1-1h3.5a1 1 0 0 1 1 1c0 1.25.2 2.45.57 3.57a1 1 0 0 1-.25 1z" fill="var(--brand-red)"/></svg>
        <span>316-555-0148</span>
      </li>
      <li class="contact__item">
        <svg class="contact__icon" viewBox="0 0 24 24" aria-hidden="true"><rect x="2" y="5" width="20" height="14" rx="1.5" fill="var(--brand-red)"/><path d="M3 6l9 7 9-7" fill="none" stroke="var(--card-black)" stroke-width="1.8"/></svg>
        <span>dan@prairiehomesforcash.com</span>
      </li>
      <li class="contact__item">
        <svg class="contact__icon" viewBox="0 0 24 24" aria-hidden="true"><g fill="none" stroke="var(--brand-red)" stroke-width="2"><circle cx="12" cy="12" r="9.5"/><ellipse cx="12" cy="12" rx="4" ry="9.5"/><path d="M2.5 12h19M4.5 7h15M4.5 17h15"/></g></svg>
        <span>www.prairiehomesforcash.com</span>
      </li>
    </ul>

    <address class="address">P.O. Box 218<br>Maple Falls, KS 67990</address>
  </section>

  <section class="card card--back" aria-label="Business card back">
    <div class="brand">
      <p class="brand__tagline">Fair offers, fast closings</p>
      <div class="brand__lockup">
        <span class="brand__dot"></span>
        <p class="brand__name">Keystone<br>Home Buyers</p>
      </div>
    </div>
  </section>

</main>
</body>
</html>
```